Vitamin Company Website Design

Seeking to create a vibrant and professional looking website for a vitamin and health food supplements business.

Morning Flintroot is a company that develops and sells vitamins and supplements for those following the "paleo" or "caveman" diet. The diet focuses upon eating organic vegetables and meat, like our ancient ancestors.

The website should emphasize health and wellness. A clean and bold design is preferred.

The website should include four sections: a home page, a blog, a community forum and an e-commerce store.

These websites communicate what we would like to look like:

http://www.korvelstudio.example/
http://www.unityassembly.example/
http://www.tlx.example/
http://www.zestkitten.example/
http://openvoiceforum.example/en/
http://tastebayoucatch.example/
http://buyrooted.example/

Target Market(s)

Health conscious men and women age 25-50

Industry/Entity Type

E-Commerce

Requirements
Must have
• The website must have 4 pages: home page, blog, community forum and online store.

The website must incorporate the company's logo, which is attached.

The company's green logo with the tagline: "Modern Wellness. Prehistoric Wisdom." is the preferred logo.

Please incorporate the other logo graphics where you see fit.
Nice to have
• Ideally, the designer will add images and/or graphics that compliment a website dedicated to health and wellness.

```html
<!DOCTYPE html>
<html lang="en">
<head>
<meta charset="utf-8">
<title>Morning Flintroot</title>
<link href="https://fonts.googleapis.com/css2?family=Ubuntu:wght@400;500&family=Open+Sans:ital,wght@0,400;0,600;1,400&display=swap" rel="stylesheet">
<style>
:root{
  --green:#8cc63f;--green-dark:#5fa219;--grey-bg:#ececec;--text:#333;--muted:#555;
  --head-grey:#6b6b6b;--line:#ddd;--panel:#f3f3f3;
}
*{margin:0;padding:0;box-sizing:border-box}
html,body{width:775px;height:1200px;overflow:hidden}
body{background:var(--grey-bg);font-family:"Open Sans",sans-serif;color:var(--text);position:relative}
.abs{position:absolute}
.page{position:absolute;left:22px;top:0;width:732px;height:1140px;background:#fff;box-shadow:0 0 4px rgba(0,0,0,.25)}
.header{position:absolute;left:0;top:0;width:732px;height:112px;background:linear-gradient(#fff,#f2f2f2)}
.brand-mark{left:34px;top:20px;width:62px;height:62px;border-radius:50%;background:var(--green)}
.brand-name{left:104px;top:32px;font-family:"Ubuntu",sans-serif;font-size:26px;font-weight:500;color:#777}
.tagline{left:104px;top:75px;font-size:10px;font-style:italic;color:#444}
.toplinks{top:10px;font-size:10px;color:#444}
.phone{left:407px;top:36px;font-size:14px;color:#444;display:flex;align-items:center;gap:5px}
.quote{left:407px;top:58px;font-size:15px;font-weight:600;color:var(--green-dark)}
.search{left:542px;top:44px;width:170px;height:23px;border:1px solid #ddd;border-radius:12px;background:#fff;font-size:8px;color:#999;padding:6px 10px}
.search .go{position:absolute;right:-1px;top:-1px;width:25px;height:25px;border-radius:50%;background:var(--green);color:#fff;font-size:9px;text-align:center;line-height:25px}
.nav{position:absolute;left:0;top:114px;width:732px;height:30px;border-top:1px solid #e5e5e5;border-bottom:1px solid #e5e5e5;display:flex;padding-left:5px;font-size:10px;background:#fff}
.nav span{padding:0 13px;line-height:28px;border-right:1px solid #e5e5e5}
.slider{position:absolute;left:0;top:146px;width:732px;height:270px;background:var(--green)}
.card{position:absolute;top:10px;width:158px;height:202px;background:#fff;border-radius:3px;box-shadow:0 4px 4px rgba(0,0,0,.15)}
.card .ph{position:absolute;left:4px;top:4px;width:150px;height:161px;border-radius:8px}
.card p{position:absolute;left:12px;top:178px;font-size:9.5px;color:#555}
.dots{left:378px;top:250px;display:flex;gap:4px}
.dots i{width:7px;height:7px;border-radius:50%;background:#fff}
.dots i:first-child{background:#222}
.latest{position:absolute;top:432px;width:312px;height:132px;background:var(--panel);border-radius:5px}
.latest h3{height:29px;background:var(--head-grey);color:#fff;font-family:"Ubuntu",sans-serif;font-weight:400;font-size:14px;padding:6px 16px;border-radius:5px 5px 0 0}
.latest .ph{position:absolute;left:8px;top:42px;width:97px;height:73px}
.latest .tx{position:absolute;left:111px;top:40px;width:196px;font-size:7.8px;line-height:15px;color:#444}
.latest .tx b{font-weight:400;font-size:9.5px;color:#333;display:block;margin-bottom:2px}
.latest .tx u{text-decoration:none;color:#222;font-size:8.5px}
.blog-title{left:16px;top:584px;font-size:13px;color:#444}
.post{position:absolute;left:16px;width:486px;height:151px;border:1px solid #ddd;border-radius:3px;background:#fff}
.post h4{position:absolute;left:14px;top:12px;font-weight:400;font-size:11.5px;color:#333}
.post .ph{position:absolute;left:22px;top:32px;width:137px;height:73px}
.post .tx{position:absolute;left:182px;top:36px;width:290px;font-size:7.8px;line-height:15px;color:#444}
.post .tx p+p{margin-top:4px}
.post .rule{position:absolute;left:22px;right:20px;top:117px;border-top:1px dotted #999}
.post .meta{position:absolute;left:26px;top:129px;font-size:8px;color:#555;display:flex;gap:20px;align-items:center}
.post .share{position:absolute;right:20px;top:128px;display:flex;gap:3px;font-size:6px}
.share span{border:1px solid #ccc;border-radius:2px;padding:1px 3px;color:#555;background:#f6f6f6}
.share .s{background:#e8502f;color:#fff;border-color:#e8502f}
.side{position:absolute;left:512px;width:211px;background:var(--panel);border-radius:3px}
.side h5{font-family:"Ubuntu",sans-serif;font-weight:400;font-size:12.5px;color:#333}
.email{width:186px;height:22px;background:#fff;border:1px solid #ccc;font-size:7px;font-style:italic;color:#999;padding:5px 15px;margin-top:8px}
.subscribe{position:absolute;right:13px;top:103px;width:66px;height:22px;background:var(--green);border:1px solid var(--green-dark);border-radius:2px;color:#fff;font-size:9px;text-align:center;line-height:20px}
.testi{position:absolute;left:9px;width:188px}
.testi .av{position:absolute;left:0;top:0;width:54px;height:50px;border:2px solid #ddd;background:linear-gradient(#9a9c8f,#574c43)}
.testi p{position:absolute;left:64px;top:0;width:126px;font-size:7.8px;line-height:13.6px;color:#555;text-align:justify}
.testi .by{position:absolute;right:0;font-size:8px;color:#a33}
.pager{left:408px;top:1113px;display:flex;gap:6px}
.pager span{height:16px;min-width:17px;padding:0 3px;background:var(--green);border:1px solid var(--green-dark);border-radius:2px;color:#333;font-size:8px;text-align:center;line-height:14px}
.social{left:33px;top:1162px;display:flex;gap:14px}
.social i{width:17px;height:17px;border-radius:2px}
.copy{right:25px;top:1161px;font-size:8px;color:#444}
</style>
</head>
<body>
<div class="page">
  <header class="header">
    <div class="abs brand-mark"></div>
    <div class="abs brand-name">Morning Flintroot</div>
    <div class="abs tagline">Modern Wellness. Prehistoric Wisdom</div>
    <div class="abs toplinks" style="left:546px">
      <svg width="12" height="10" viewBox="0 0 12 10" style="vertical-align:-1px"><path d="M0 1h2l2 6h6l1.5-4.5H3" fill="none" stroke="#222" stroke-width="1.3"/><circle cx="5" cy="9" r="1" fill="#222"/><circle cx="9" cy="9" r="1" fill="#222"/></svg> My Cart</div>
    <div class="abs toplinks" style="left:614px">Order</div>
    <div class="abs toplinks" style="left:661px">
      <svg width="11" height="11" viewBox="0 0 11 11" style="vertical-align:-1px"><circle cx="5.5" cy="3" r="2.6" fill="#222"/><path d="M0 11a5.5 5 0 0 1 11 0z" fill="#222"/></svg> Account</div>
    <div class="abs phone"><svg width="18" height="14" viewBox="0 0 18 14"><path d="M2 3c3-3 11-3 14 0l-2 3-3-1V3H7v2l-3 1z" fill="#555" transform="rotate(30 9 7)"/></svg>03 4812 2296</div>
    <div class="abs quote">Free Quotes Call</div>
    <div class="abs search">Enter keyword<span class="go">GO</span></div>
  </header>
  <nav class="nav"><span>Home</span><span>News</span><span>Recipes</span><span>Home Cooking</span><span>Videos</span><span>Cooking Tips</span><span>Eat Out</span><span>Contact Us</span><span>Wedding</span><span>Advertise</span></nav>

  <section class="slider">
    <div class="card" style="left:18px"><div class="ph" role="img" aria-label="Sliced citrus fruits, kiwi and strawberries" style="background:linear-gradient(135deg,#f6a21f,#e9d35a 50%,#c8322a)"></div><p>Loreum Ipsum Dollar</p></div>
    <div class="card" style="left:196px"><div class="ph" role="img" aria-label="Amber supplement capsules" style="background:radial-gradient(circle at 60% 60%,#c8281c,#e89456 60%,#f2d9b8)"></div><p>Loreum Ipsum Dollar</p></div>
    <div class="card" style="left:375px"><div class="ph" role="img" aria-label="Cheese, poultry, eggs, pasta and bread" style="background:linear-gradient(135deg,#e8c462,#e9c9a6 55%,#b28a5e)"></div><p>Loreum Ipsum Dollar</p></div>
    <div class="card" style="left:557px"><div class="ph" role="img" aria-label="Woman eating a fresh salad" style="background:linear-gradient(135deg,#3b3b3b,#e7d6cc 45%,#7fb94a)"></div><p>Loreum Ipsum Dollar</p></div>
    <div class="abs dots"><i></i><i></i><i></i><i></i></div>
  </section>

  <article class="latest" style="left:36px"><h3>Latest Blog Articles</h3>
    <div class="ph" role="img" aria-label="Spilled supplement bottle with capsules" style="background:linear-gradient(135deg,#cde8ef,#e9e05a 60%,#5e9e3a)"></div>
    <div class="tx"><b>Duis non nunc &nbsp;| &nbsp;13 Oct &nbsp;2012</b>Nulla rhoncus dictum metus. Curabitur tristique mi condimentum orci. Phasellus pellentesque aliquam enim. Proin dui mattis laoreet,<br><u>learn more</u></div></article>
  <article class="latest" style="left:378px"><h3>Latest Blog Articles</h3>
    <div class="ph" role="img" aria-label="Glass of milk with fresh fruits" style="background:linear-gradient(#1a1a1a,#f0f0f0 45%,#d96a2a 80%)"></div>
    <div class="tx"><b>Duis non nunc &nbsp;| &nbsp;13 Oct &nbsp;2012</b>Nulla rhoncus dictum metus. Curabitur tristique mi condimentum orci. Phasellus pellentesque aliquam enim. Proin dui mattis laoreet,<br><u>learn more</u></div></article>

  <h2 class="abs blog-title" style="font-weight:400">BLOG</h2>

  <article class="post" style="top:612px"><h4>Duis non nunc Nulla rhoncus dictum metus.</h4>
    <div class="ph" role="img" aria-label="Salmon and steak on a plate" style="background:linear-gradient(#e7e1dc,#f0a45c 45%,#8b3a2e)"></div>
    <div class="tx"><p>Curabitur tristique mi condimentum orci. Phasellus pellentesque aliquam enim. Proin dui lectus, cursus eu, mattis laoreet, viverra sit amet, quam.</p><p>Curabitur tristique mi condimentum orci. Phasellus pellentesque aliquam enim. Proin dui lectus, cursus eu, mattis laoreet, viverra sit amet, quam.</p></div>
    <div class="rule"></div>
    <div class="meta"><span>&#9635; 13 Oct</span><span>&#9829; 23 Notes</span></div>
    <div class="share"><span>Like</span><span>3k</span><span>Post</span><span>316</span><span>Vote</span><span>81</span><span class="s">Share</span><span>4.6K</span></div></article>

  <article class="post" style="top:779px"><h4>Duis non nunc Nulla rhoncus dictum metus.</h4>
    <div class="ph" role="img" aria-label="Bread rolls with herb dip and lemon" style="background:linear-gradient(135deg,#8eaa3a,#d6a35c 50%,#e9d774)"></div>
    <div class="tx"><p>Curabitur tristique mi condimentum orci. Phasellus pellentesque aliquam enim. Proin dui lectus, cursus eu, mattis laoreet, viverra sit amet, quam.</p><p>Curabitur tristique mi condimentum orci. Phasellus pellentesque aliquam enim. Proin dui lectus, cursus eu, mattis laoreet, viverra sit amet, quam.</p></div>
    <div class="rule"></div>
    <div class="meta"><span>&#9635; 13 Oct</span><span>&#9829; 23 Notes</span></div>
    <div class="share"><span>Like</span><span>3k</span><span>Post</span><span>316</span><span>Vote</span><span>81</span><span class="s">Share</span><span>4.6K</span></div></article>

  <article class="post" style="top:946px"><h4>Duis non nunc Nulla rhoncus dictum metus.</h4>
    <div class="ph" role="img" aria-label="Bowl of spicy shrimp soup with herbs" style="background:radial-gradient(circle,#e0562a,#c83a1f 60%,#efe4d8)"></div>
    <div class="tx"><p>Curabitur tristique mi condimentum orci. Phasellus pellentesque aliquam enim. Proin dui lectus, cursus eu, mattis laoreet, viverra sit amet, quam.</p><p>Curabitur tristique mi condimentum orci. Phasellus pellentesque aliquam enim. Proin dui lectus, cursus eu, mattis laoreet, viverra sit amet, quam.</p></div>
    <div class="rule"></div>
    <div class="meta"><span>&#9635; 13 Oct</span><span>&#9829; 23 Notes</span></div>
    <div class="share"><span>Like</span><span>3k</span><span>Post</span><span>316</span><span>Vote</span><span>81</span><span class="s">Share</span><span>4.6K</span></div></article>

  <aside class="side" style="top:612px;height:132px;padding:16px 12px">
    <h5 style="padding-left:6px">Sign Up to Stay in Touch</h5>
    <p style="font-size:7.5px;line-height:13px;margin:10px 0 0 6px;color:#333">Please enter your email address below to sign up for our mailing list.</p>
    <div class="email">your email address here..</div>
    <div class="subscribe">Subscribe &rsaquo;</div>
  </aside>

  <aside class="side" style="top:760px;height:272px">
    <h5 style="position:absolute;left:16px;top:8px;font-size:13px">Testimonials</h5>
    <div class="testi" style="top:42px"><div class="av" role="img" aria-label="Customer portrait"></div>
      <p>Nunc varius facilisis eros. Sed erat. In in velit quis arcu ornare laoreet. Curabitur adipiscing luctus massa. Integer ut purus ac commodo</p>
      <span class="by" style="top:64px">— Marcus Hale</span></div>
    <div class="testi" style="top:141px"><div class="av" role="img" aria-label="Customer portrait outdoors" style="background:linear-gradient(#5f7f3a,#c9b49b)"></div>
      <p>Nunc varius facilisis eros. Sed erat. In in velit quis arcu ornare laoreet. Curabitur adipiscing luctus massa.Integer ut purus ac commodo</p>
      <span class="by" style="top:83px">— Marcus Hale</span></div>
    <span class="abs" style="right:12px;top:250px;font-size:8px;color:var(--green-dark)">READ MORE</span>
  </aside>

  <div class="abs pager"><span>1</span><span>2</span><span>3</span><span style="margin-left:6px">10</span></div>
</div>

<div class="abs social"><i style="background:#3b5998"></i><i style="background:#4aa8e0"></i><i style="background:#f26b21"></i><i style="background:#0e6fa5"></i><i style="background:#d6453a"></i></div>
<div class="abs copy">© 2012 Morning Flintroot All right reserved</div>
</body>
</html>
```